KORBALT

The business want a professional looking business card. We have a scetch we will add but want the extra upgrade, and would like more suggestions for variations of our business cards.

```html
<!DOCTYPE html>
<html lang="en">
<head>
<meta charset="utf-8">
<title>KORBALT business card</title>
<link rel="stylesheet" href="https://fonts.googleapis.com/css2?family=Marcellus&family=Montserrat:wght@500;700&family=Roboto+Condensed:wght@500&display=swap">
<style>
  :root {
    --page: #ffffff;
    --card: #000000;
    --gold: #c8ab74;
    --gold-light: #e0cfa6;
    --gold-line: #a88a55;
  }
  * { margin: 0; padding: 0; box-sizing: border-box; }
  html, body { width: 1200px; height: 1200px; overflow: hidden; background: var(--page); }
  .canvas {
    width: 1200px; height: 1200px;
    display: flex; flex-direction: column; align-items: center; justify-content: center;
    gap: 48px;
  }
  .card {
    position: relative;
    width: 860px; height: 528px;
    background: var(--card);
    overflow: hidden;
  }
  /* front */
  .front-brand {
    position: absolute; left: 0; right: 0; top: 190px;
    text-align: center;
    font-family: "Marcellus", serif;
    font-size: 92px; letter-spacing: 30px; padding-left: 30px;
    color: var(--gold);
    line-height: 1;
  }
  .front-since {
    position: absolute; left: 0; right: 0; top: 322px;
    text-align: center;
    font-family: "Montserrat", sans-serif; font-weight: 700;
    font-size: 26px; letter-spacing: 18px; padding-left: 18px;
    color: var(--gold-light);
  }
  /* back */
  .back-title {
    position: absolute; left: 0; right: 0; top: 34px;
    text-align: center;
    font-family: "Marcellus", serif;
    font-size: 50px; letter-spacing: 3px;
    color: var(--gold);
  }
  .back-title .surname { color: var(--gold-light); }
  .divider {
    position: absolute; left: 430px; top: 118px;
    width: 3px; height: 378px;
    background: linear-gradient(var(--gold-line), var(--gold-light), var(--gold-line));
  }
  .person-name {
    position: absolute; left: 34px; top: 182px;
    font-family: "Marcellus", serif;
    font-size: 29px; color: var(--gold);
    border-bottom: 2px solid var(--gold);
    line-height: 1.05; padding-right: 4px;
  }
  .person-role {
    position: absolute; left: 34px; top: 221px;
    font-family: "Montserrat", sans-serif; font-weight: 500;
    font-size: 19px; letter-spacing: 1.5px; color: var(--gold);
  }
  .contact-list { position: absolute; left: 34px; top: 302px; list-style: none; }
  .contact-item {
    display: flex; align-items: center; gap: 14px;
    height: 52px;
    font-family: "Roboto Condensed", sans-serif; font-weight: 500;
    font-size: 25px; color: var(--gold-light);
  }
  .contact-icon { width: 32px; height: 32px; flex: none; }
  .back-brand {
    position: absolute; left: 450px; right: 0; top: 352px;
    display: flex; flex-direction: column; align-items: center;
  }
  .brand-dot {
    width: 92px; height: 92px; border-radius: 50%;
    background: var(--gold);
    margin-bottom: 36px; margin-top: -140px;
  }
  .back-brand-name {
    font-family: "Marcellus", serif;
    font-size: 46px; letter-spacing: 12px; padding-left: 12px;
    color: var(--gold); line-height: 1;
  }
  .back-brand-since {
    margin-top: 12px;
    font-family: "Montserrat", sans-serif; font-weight: 700;
    font-size: 13px; letter-spacing: 9px; padding-left: 9px;
    color: var(--gold-light);
  }
</style>
</head>
<body>
<main class="canvas">
  <section class="card card-front">
    <div class="front-brand">KORBALT</div>
    <div class="front-since">SINCE 2026</div>
  </section>

  <section class="card card-back">
    <h1 class="back-title">KORBALT <span class="surname">BREKKESTAD</span></h1>
    <div class="person-name">MATS OLAV BREKKESTAD</div>
    <div class="person-role">CEO &amp; FOUNDER</div>

    <ul class="contact-list">
      <li class="contact-item">
        <svg class="contact-icon" viewBox="0 0 32 32" fill="none" stroke="#c8ab74" stroke-width="1.6">
          <circle cx="16" cy="16" r="14.5"/>
          <path d="M16 24c-4-5-6-8-6-11a6 6 0 0 1 12 0c0 3-2 6-6 11z"/>
          <circle cx="16" cy="13" r="2.2"/>
        </svg>Address</li>
      <li class="contact-item">
        <svg class="contact-icon" viewBox="0 0 32 32" fill="none" stroke="#c8ab74" stroke-width="1.6">
          <circle cx="16" cy="16" r="14.5"/>
          <path d="M11 9l3 0 1.5 4-2 1.5c1 2 2 3 4 4l1.5-2 4 1.5v3c-6 1-13-6-12-12z"/>
        </svg>Phone number</li>
      <li class="contact-item">
        <svg class="contact-icon" viewBox="0 0 32 32" fill="none" stroke="#c8ab74" stroke-width="1.6">
          <circle cx="16" cy="16" r="14.5"/>
          <rect x="9" y="11" width="14" height="10"/>
          <path d="M9 11l7 6 7-6"/>
        </svg>e-mail</li>
      <li class="contact-item">
        <svg class="contact-icon" viewBox="0 0 32 32" fill="none" stroke="#c8ab74" stroke-width="1.6">
          <circle cx="16" cy="16" r="14.5"/>
          <circle cx="16" cy="16" r="7"/>
          <ellipse cx="16" cy="16" rx="3" ry="7"/>
          <path d="M9 16h14"/>
        </svg>Website</li>
    </ul>

    <div class="divider"></div>

    <div class="back-brand">
      <div class="brand-dot"></div>
      <div class="back-brand-name">KORBALT</div>
      <div class="back-brand-since">SINCE 2026</div>
    </div>
  </section>
</main>
</body>
</html>
```